Elegant, High End Integrated Wellness Healthcare Practice

We need a brochure designed for an integrated mind-body wellness healthcare practice (www.larkfernclinic.com) . This brochure will be used when we cold call prospects (physicians to refer to our office, and potential consumers to utilize our services). Our practice is geographically located in the middle Tennessee USA region, although we have plans to become an international company as many of our offerings can be accessed anywhere in the world. Ultimately our goal is to have this brochure used as a leave-behind in an effort to introduce our integrated offerings to increase market share. The final product brochure should be both elegant and serious, with clean lines but also convey warmth and trust, as individuals who are coming for our services have usually struggled with their health for a significant amount of time before finding our practice.
Updates

The design brief was very specific about providing a high-end science-based 2-page brochure (not flier). Several designs submitted were fliers. The other designs were heavy on yoga or "woo woo" non-science-based looking pictures. This is a flier to appeal to physicians and other healthcare providers. Therefore the design must speak science and evidence-based methods of mind and body wellness care. I would also like to appeal to the other designers I paid extra for their submissions and who have indicated they will "respond in the coming days."

```html
<!DOCTYPE html>
<html lang="en">
<head>
<meta charset="utf-8">
<title>Larkfern Clinic Brochure</title>
<link rel="stylesheet" href="https://fonts.googleapis.com/css2?family=Cinzel:wght@400;700&family=Roboto:wght@400&family=Noto+Serif:wght@700&display=swap">
<style>
  :root{
    --page:#ffffff;
    --ink:#000000;
    --leaf:#5b8f2f;
    --leaf-deep:#4a7a28;
    --heading:#6a9a35;
    --label:#4f7a2c;
    --text:#ffffff;
    --photo-sky:#b9c6cc;
    --photo-field:#7f9a4a;
  }
  *{box-sizing:border-box;margin:0;padding:0}
  html,body{width:788px;height:1200px;overflow:hidden;background:var(--page)}
  .stage{position:absolute;left:0;top:0;width:1440px;height:2193px;transform:scale(.5472);transform-origin:0 0}
  .view-label{position:absolute;font-family:"Cinzel",serif;font-weight:400;color:var(--label);font-size:84px;line-height:1;letter-spacing:1px}
  .spread{position:absolute;width:1224px;height:791px;overflow:hidden;background:var(--ink)}
  .spread svg.bg{position:absolute;left:0;top:0}
  .fold{position:absolute;top:0;width:1px;height:100%;background:#2a3d1c}
  .abs{position:absolute}
  .section-title{font-family:"Cinzel",serif;font-weight:700;color:var(--heading);font-size:24px;letter-spacing:.5px;white-space:nowrap}
  .section-title.light{font-weight:400;font-size:26px}
  .rule{position:absolute;height:1px;background:var(--heading)}
  .body-copy{font-family:"Roboto",sans-serif;color:var(--text);font-size:17.5px}
  .services{list-style:none;font-family:"Roboto",sans-serif;color:var(--text);font-size:20px}
  .services li{position:relative;padding-left:28px;height:32px;line-height:32px;white-space:nowrap}
  .services li::before{content:"";position:absolute;left:0;top:8px;width:17px;height:17px;border-radius:50%;background:var(--text)}
  .brand{font-family:"Cinzel",serif;font-weight:400;color:var(--leaf-deep);font-size:25px;line-height:38px;white-space:nowrap}
  .brand-dot{position:absolute;border-radius:50%;background:var(--leaf-deep)}
  .headline{font-family:"Cinzel",serif;font-weight:700;color:var(--text);font-size:26px;line-height:33px;text-align:center;text-shadow:0 1px 3px rgba(0,0,0,.45)}
  .contact{font-family:"Noto Serif",serif;font-weight:700;color:var(--text);font-size:22px;line-height:30px;text-align:center}
  .team-title{font-family:"Cinzel",serif;font-weight:700;color:var(--text);font-size:36px;white-space:nowrap}
  .portrait{position:absolute;border:3px solid var(--text)}
  .member{position:absolute;font-family:"Roboto",sans-serif;color:var(--text);font-size:20px;text-align:center;width:240px}
</style>
</head>
<body>
<main class="stage">

  <div class="view-label" style="left:298px;top:88px">Back</div>
  <div class="view-label" style="left:875px;top:88px">Front</div>

  <section class="spread outer" style="left:100px;top:231px">
    <svg class="bg" width="1224" height="791" viewBox="0 0 1224 791">
      <defs>
        <linearGradient id="field" x1="0" y1="0" x2="0" y2="1">
          <stop offset="0" stop-color="var(--photo-sky)"/>
          <stop offset=".45" stop-color="#8c9a7c"/>
          <stop offset="1" stop-color="var(--photo-field)"/>
        </linearGradient>
      </defs>
      <path fill="var(--leaf)" d="M0,150 C40,380 170,590 420,640 C560,668 690,700 735,791 L0,791 Z"/>
      <path fill="var(--leaf)" d="M318,0 L530,0 C570,160 660,270 800,350 C930,420 1080,455 1224,460 L1224,791 C1170,690 1090,610 950,560 C820,520 700,460 600,380 C470,280 370,150 318,0 Z"/>
      <path fill="var(--ink)" d="M1224,520 L1224,791 L1210,791 C1160,700 1080,640 960,600 L960,570 C1080,590 1170,560 1224,520 Z"/>
      <path role="img" aria-label="Photo of a woman breathing fresh air in a green field" fill="url(#field)" d="M680,0 L1224,0 L1224,440 C1040,445 860,400 760,250 C715,180 690,90 680,0 Z"/>
      <path fill="none" stroke="var(--ink)" stroke-width="18" d="M672,0 C682,95 706,185 752,258 C855,412 1040,456 1224,452"/>
    </svg>
    <div class="fold" style="left:601px"></div>

    <h2 class="abs section-title" style="left:26px;top:46px">Our Unique Approach:</h2>
    <div class="rule" style="left:38px;top:82px;width:268px"></div>
    <p class="abs body-copy" style="left:33px;top:113px;width:565px;line-height:30px">At Larkfern Clinic we Facilitate body and mind health and wellness through an integrated functional approach to care.This method of personalized care appreciates you as a unique individual with distinct health circumstances. We tailor our body and mind approaches to address your specific healthconcerns. The result is integrative healing-oriented care that addresses aspect of your whole person (body, mind, and spirit).</p>

    <div class="brand-dot" style="left:300px;top:445px;width:24px;height:24px;background:var(--heading)"></div>
    <div class="abs brand" style="left:334px;top:437px;color:var(--heading);font-size:27px">Larkfern Clinic</div>

    <div class="abs contact" style="left:95px;top:682px;width:450px">
      <svg width="20" height="28" viewBox="0 0 20 28" style="vertical-align:-3px;margin-right:10px"><path fill="#fff" d="M10,0 C4.5,0 0,4.4 0,9.8 C0,17 10,28 10,28 C10,28 20,17 20,9.8 C20,4.4 15.5,0 10,0 Z M10,14 A4.2,4.2 0 1 1 10,5.6 A4.2,4.2 0 1 1 10,14 Z"/></svg>418 Willow Bend Rd. Franklin,<br>TN 37064<br>
      <svg width="24" height="24" viewBox="0 0 24 24" style="vertical-align:-3px;margin-right:4px"><path fill="#fff" d="M6.6,10.8 C8,13.6 10.4,16 13.2,17.4 L15.4,15.2 C15.7,14.9 16.1,14.8 16.4,15 C17.5,15.4 18.8,15.6 20,15.6 C20.6,15.6 21,16 21,16.6 L21,20 C21,20.6 20.6,21 20,21 C10.6,21 3,13.4 3,4 C3,3.4 3.4,3 4,3 L7.5,3 C8.1,3 8.5,3.4 8.5,4 C8.5,5.3 8.7,6.5 9.1,7.6 C9.2,7.9 9.1,8.3 8.9,8.6 Z"/></svg>(615) 555-0142, (615) 555-0187
    </div>

    <div class="brand-dot" style="left:935px;top:24px;width:70px;height:70px"></div>
    <div class="abs brand" style="left:1015px;top:22px">Larkfern<br>Clinic</div>

    <h1 class="abs headline" style="left:925px;top:198px;width:290px">Integrated Body<br>&amp;<br>Mind Health,<br>Wellness Center</h1>

    <h2 class="abs section-title" style="left:618px;top:460px">Our Services:</h2>
    <div class="rule" style="left:618px;top:494px;width:185px"></div>
    <ul class="abs services" style="left:650px;top:512px"><li>Whole Body wellness</li><li>Brain Wave Mapping</li></ul>
    <ul class="abs services" style="left:965px;top:512px"><li>Wellness Package</li><li>Nutritional Wellness</li></ul>

    <h2 class="abs section-title" style="left:610px;top:596px">Featured Services:</h2>
    <div class="rule" style="left:622px;top:630px;width:245px"></div>
    <ul class="abs services" style="left:650px;top:645px"><li>Sonal Brain care</li><li>Functional Medicine</li></ul>
    <ul class="abs services" style="left:963px;top:643px"><li>Healthy Lifestyle</li><li style="margin-top:6px">Lumara for Pain</li></ul>
  </section>

  <div class="view-label" style="left:510px;top:1052px">Inner Side</div>

  <section class="spread inner" style="left:96px;top:1168px">
    <svg class="bg" width="1224" height="791" viewBox="0 0 1224 791">
      <path fill="var(--leaf-deep)" d="M0,200 C40,480 200,680 450,700 C560,710 640,745 680,791 L0,791 Z"/>
      <path fill="var(--leaf-deep)" d="M510,0 L1224,0 L1224,630 C1150,500 1010,380 870,300 C730,220 600,130 510,0 Z"/>
    </svg>
    <div class="fold" style="left:606px"></div>

    <h2 class="abs section-title light" style="left:34px;top:104px">What we do at Larkfern Clinic</h2>
    <div class="rule" style="left:48px;top:142px;width:478px"></div>
    <p class="abs body-copy" style="left:29px;top:174px;width:555px;line-height:36px">Larkfern Clinic is different than traditional health practice. Our approach toward health and wellness looks at the whole person and the interaction of each aspect of your being with the other.We have core values that are the backbone of effective integrated care.</p>

    <div class="abs" role="img" aria-label="Icons: healthy body plus healthy mind equals happy human" style="left:200px;top:378px;width:326px;height:160px;background:linear-gradient(90deg,#2a2a2a,#3c3c3c);border-radius:6px"></div>

    <h2 class="abs team-title" style="left:770px;top:58px">Meet Our Team</h2>
    <div class="rule" style="left:790px;top:104px;width:268px;background:var(--text)"></div>

    <div class="portrait" role="img" aria-label="Portrait of Dr. Anna Price" style="left:704px;top:128px;width:170px;height:160px;border:none;background:linear-gradient(160deg,#d9d7d2,#8a9ac0)"></div>
    <div class="portrait" role="img" aria-label="Portrait of Dr. Paul Hartley" style="left:924px;top:128px;width:176px;height:164px;background:linear-gradient(160deg,#9b8f7e,#2c3440)"></div>
    <div class="member" style="left:669px;top:308px">Dr. Anna Price</div>
    <div class="member" style="left:930px;top:308px">Dr. Paul Hartley</div>
    <div class="portrait" role="img" aria-label="Portrait of Megan Carver" style="left:818px;top:350px;width:176px;height:168px;background:linear-gradient(160deg,#6a5a4a,#c8a88e)"></div>
    <div class="member" style="left:791px;top:532px">Megan Carver</div>

    <h2 class="abs section-title light" style="left:640px;top:596px">What we treat at Larkfern Clinic</h2>
    <div class="rule" style="left:660px;top:633px;width:490px"></div>
    <p class="abs body-copy" style="left:657px;top:654px;width:535px;line-height:36px">Larkfern Clinic provides treatment for a full scope of psychiatric &amp; cognitive conditions, attention, distractibility, learning concerns, and various complex chronic conditions</p>
  </section>

</main>
</body>
</html>
```